Law Firm Website

Our client has never had a website, but their services are similar to: https://www.tallbrook-vance.com.

They are a personal injury attorney, husband, and wife team.

Coding

Coded - Design and coding required

Number of Pages Required

1 page

Font styles to use
Sans Serif

Colors
0054AA
0677BA
7BADD7
CADEEF
E8F1F8

```html
<!DOCTYPE html>
<html lang="en">
<head>
<meta charset="utf-8">
<title>Brightline Law — Personal Injury Attorneys</title>
<link href="https://fonts.googleapis.com/css2?family=Lato:wght@300;400;700;900&display=swap" rel="stylesheet">
<style>
:root{
  --blue:#0054AA;
  --blue-mid:#0677BA;
  --blue-soft:#7BADD7;
  --blue-pale:#CADEEF;
  --blue-mist:#E8F1F8;
  --navy:#0c2a55;
  --navy-deep:#0a2146;
  --ink:#1d2b3a;
  --text:#3c4652;
  --white:#ffffff;
}
*{box-sizing:border-box;margin:0;padding:0}
html,body{width:1200px;height:4386px;overflow:hidden}
body{position:relative;font-family:"Lato",Arial,sans-serif;color:var(--text);background:var(--white)}
.abs{position:absolute}
a{color:inherit;text-decoration:none}

/* top bar */
.topbar{top:0;left:0;width:1200px;height:34px;background:var(--navy-deep)}
.topbar-light{top:0;left:0;width:500px;height:34px;background:var(--blue-mist);clip-path:polygon(0 0,100% 0,94% 100%,0 100%)}
.stay{top:11px;left:133px;font-size:11px;color:var(--ink);letter-spacing:.3px}
.social-dots{top:7px;left:254px;display:flex;gap:6px}
.dot-icon{width:20px;height:20px;border-radius:50%;background:var(--blue)}
.top-contact{top:11px;font-size:11px;color:var(--white);display:flex;align-items:center;gap:6px}

/* header */
.header{top:34px;left:0;width:1200px;height:82px;background:var(--white)}
.brand{font-weight:700;color:var(--blue);letter-spacing:4px;line-height:1;text-align:center}
.brand small{display:block;font-size:13px;letter-spacing:7px;margin-top:4px;font-weight:700}
.header-brand{top:60px;left:133px;font-size:21px}
.nav{top:71px;left:392px;display:flex;font-size:12px;color:#55606c}
.nav span{margin-right:22px}
.nav .active{color:var(--blue);font-weight:700}
.callbox{top:52px;left:948px;color:var(--blue)}
.callbox .small{font-size:10px;color:var(--ink)}
.callbox .phone{font-size:19px;font-weight:400;margin:3px 0 2px}

/* hero */
.hero{top:116px;left:0;width:1200px;height:553px;background:linear-gradient(180deg,#3a4656 0%,#55606c 40%,#2f3b4c 100%)}
.hero-shade{top:116px;left:0;width:1200px;height:553px;background:radial-gradient(ellipse at center,rgba(10,33,70,.35),rgba(10,33,70,.6))}
.rule{height:1px;background:var(--blue-mid)}
.rule.dl::before,.rule.dr::after{content:"";position:absolute;top:-3px;width:7px;height:7px;border-radius:50%;background:var(--blue-mid)}
.rule.dl::before{left:-3px}
.rule.dr::after{right:-3px}
.hero-kicker{top:318px;left:0;width:1200px;text-align:center;color:var(--white);font-size:19px;letter-spacing:9px}
.hero-title{top:368px;left:0;width:1200px;text-align:center;color:var(--white);font-size:46px;font-weight:900;letter-spacing:1px}
.hero-sub{top:428px;left:0;width:1200px;text-align:center;color:var(--white);font-size:18px;font-weight:700}
.btn{background:var(--blue);color:var(--white);font-weight:700;font-size:14px;letter-spacing:.5px;display:flex;align-items:center;justify-content:center}
.hero-btn{top:475px;left:531px;width:138px;height:36px}

/* about */
.about{top:669px;left:0;width:1060px;height:611px;background:var(--navy)}
.about-tab{top:715px;left:1060px;width:140px;height:468px;background:var(--navy-deep)}
.vertical{writing-mode:vertical-rl;font-weight:900;letter-spacing:2px}
.vertical.up{transform:rotate(180deg)}
.about-tab .vertical{position:absolute;left:46px;top:120px;color:var(--white);font-size:40px}
.photo{display:block}
.about-photo{top:754px;left:194px;width:363px;height:429px;background:linear-gradient(160deg,#6b5a4c,#a8876b 45%,#3d3631)}
.about-photo-small{top:1009px;left:134px;width:197px;height:164px;border:4px solid var(--white);background:linear-gradient(135deg,#2a1a10,#7a4a28 50%,#1b120c)}
.about-title{top:798px;left:590px;font-size:37px;color:var(--white);letter-spacing:2px;font-weight:400}
.about-copy{top:874px;left:590px;width:430px;font-size:12px;line-height:20.5px;color:var(--white)}
.about-copy p+p{margin-top:20px}
.about-btn{top:1093px;left:590px;width:208px;height:39px}

/* stats */
.section-title{font-size:37px;color:var(--ink);letter-spacing:2px;text-align:center;width:1200px;left:0;font-weight:400}
.stats{top:1433px;left:168px;display:flex;gap:20px}
.stat{width:201px;height:135px;background:var(--navy-deep);color:var(--white);text-align:center;padding-top:14px}
.stat.featured{background:var(--blue)}
.stat .num{font-size:60px;font-weight:400;line-height:1.1}
.stat .label{font-size:16px;margin-top:4px}

/* practice */
.practice{top:1649px;left:148px;width:1052px;height:761px;background:linear-gradient(160deg,#123463,#0d2a55 60%,#0a2248)}
.practice-vertical{top:1835px;left:50px;color:var(--navy-deep);font-size:40px}
.practice-title{top:1722px;left:148px;width:910px;text-align:center;font-size:37px;color:var(--white);letter-spacing:2px;font-weight:400}
.cards{left:179px;display:grid;grid-template-columns:repeat(4,201px);column-gap:13px}
.card{position:relative;height:196px}
.card .shot{position:absolute;top:0;left:0;width:201px;height:136px}
.card .label{position:absolute;top:133px;left:9px;width:183px;height:59px;background:var(--white);display:flex;align-items:center;justify-content:center;text-align:center;font-weight:900;font-size:14px;color:var(--ink);letter-spacing:.5px;line-height:1.2}
.card .plus{position:absolute;top:185px;left:90px;width:21px;height:21px;border-radius:50%;background:var(--blue-mid);color:var(--white);font-weight:700;font-size:17px;line-height:17px;text-align:center;border:2px solid var(--white)}
.practice-btn{top:2291px;left:490px;width:223px;height:37px}

/* testimonials */
.testi-panel{top:2493px;left:209px;width:851px;height:464px;background:var(--blue-mist)}
.badge-cell{width:209px;height:155px;background:var(--white);border:1px solid #dfe5ec;display:flex;align-items:center;justify-content:center}
.badge-shape{width:84px;height:84px;border-radius:50%;background:var(--blue-pale)}
.badge-shape.square{border-radius:4px;width:100px;height:64px}
.testi-vertical{top:2555px;left:1104px;color:var(--navy-deep);font-size:40px}
.testi-title{top:2553px;left:700px;width:330px;text-align:right;font-size:37px;color:var(--ink);letter-spacing:2px;line-height:1.18;font-weight:400}
.testi-copy{top:2677px;left:488px;width:542px;font-size:12px;line-height:18.8px;color:var(--text)}
.author{top:2859px;left:490px;display:flex;align-items:center;gap:8px;font-weight:900;font-size:14px;color:var(--ink)}
.avatar{width:30px;height:30px;border-radius:50%;background:linear-gradient(135deg,#c99c84,#8a5a48)}
.stars{top:2896px;left:490px;display:flex;gap:9px}

/* blog */
.blog{top:3104px;left:168px;display:flex;gap:5px}
.post{position:relative;width:285px;height:247px}
.post .shot{position:absolute;inset:0}
.post .meta{position:absolute;left:54px;bottom:0;width:231px;height:54px;background:var(--white);padding:6px 10px 0;font-size:10px;line-height:12px;color:var(--ink)}
.post .meta-row{display:flex;justify-content:space-between;font-size:8.5px;margin-bottom:6px;align-items:center}

/* contact */
.start{top:3504px;left:0;width:1200px;height:496px;background:var(--navy)}
.start-panel{top:3579px;left:0;width:599px;height:421px;background:var(--navy-deep)}
.start-photo{top:3392px;left:715px;width:340px;height:451px;background:linear-gradient(180deg,#d8dde4 0%,#b9c5d3 30%,#23477d 62%,#163666 100%);border-radius:160px 160px 0 0}
.start-call{top:3843px;left:599px;width:601px;height:157px;background:var(--blue)}
.start-title{top:3630px;left:167px;font-size:33px;color:var(--white);letter-spacing:2px;font-weight:400}
.start-lead{top:3690px;left:168px;width:400px;font-size:12px;line-height:19px;color:var(--white)}
.field{height:31px;background:var(--white);font-size:9px;color:#9aa3ad;padding:10px 12px}
.field.big{height:85px}
.submit{top:3926px;left:420px;width:145px;height:36px}
.call-copy{top:3876px;left:648px;width:460px;font-size:15px;line-height:24px;color:var(--white);font-weight:700}
.call-line{top:3939px;left:648px;display:flex;align-items:center;gap:7px;color:var(--white);font-size:12px;font-weight:700}
.call-line strong{font-size:20px;font-weight:400}

/* footer */
.footer{top:4000px;left:0;width:1200px;height:386px;background:var(--navy-deep)}
.footer-brand{top:4047px;left:172px;font-size:25px;color:var(--white)}
.footer-brand small{font-size:15px;letter-spacing:9px}
.footer-social{top:4118px;left:170px;display:flex;gap:18px}
.footer-social .dot-icon{width:26px;height:26px;background:var(--blue)}
.fcol{top:4046px;color:var(--white)}
.fcol h4{font-size:13px;font-weight:700;margin-bottom:18px}
.fcol li{list-style:none;font-size:10.5px;height:25px}
.contact-row{display:flex;gap:8px;font-size:10.5px;line-height:15px;margin-bottom:12px}
.footer-line{top:4270px;left:168px;width:864px;height:1px;background:rgba(255,255,255,.08)}
.copyright{top:4281px;left:168px;font-size:10px;color:var(--white)}
.copyright b{color:var(--blue-soft);font-weight:400}
.legal{top:4281px;left:855px;font-size:10px;color:var(--white)}
.fineprint{top:4313px;left:168px;width:864px;font-size:8.5px;line-height:15px;color:#c6d2e0}
</style>
</head>
<body>

<!-- top bar -->
<div class="abs topbar"></div>
<div class="abs topbar-light"></div>
<div class="abs stay">STAY CONNECTED</div>
<div class="abs social-dots"><span class="dot-icon"></span><span class="dot-icon"></span><span class="dot-icon"></span><span class="dot-icon"></span><span class="dot-icon"></span></div>
<div class="abs top-contact" style="left:730px">
  <svg width="12" height="9" viewBox="0 0 12 9" fill="none" stroke="#fff" stroke-width="1"><rect x=".5" y=".5" width="11" height="8"/><path d="M.5 .5l5.5 4.5 5.5-4.5"/></svg>
  info@brightlinelaw.com
</div>
<div class="abs top-contact" style="left:914px">
  <svg width="9" height="12" viewBox="0 0 9 12" fill="none" stroke="#fff" stroke-width="1"><path d="M4.5 11.5S.5 7 .5 4.5a4 4 0 0 1 8 0c0 2.5-4 7-4 7z"/><circle cx="4.5" cy="4.5" r="1.4"/></svg>
  48 Harbor Lane, NC 27000
</div>

<!-- header -->
<div class="abs header"></div>
<div class="abs brand header-brand">BRIGHTLINE<small>LAW</small></div>
<nav class="abs nav"><span class="active">Home</span><span>About</span><span>Areas of Practise</span><span>Blog</span><span>Resources</span><span style="margin-right:10px">Contat</span><span>Client Portal</span></nav>
<div class="abs callbox"><div class="small">CALL NOW FOR YOUR</div><div class="phone">(555)014-2286</div><div class="small">FREE CONSULTATION</div></div>

<!-- hero -->
<div class="abs hero photo" role="img" aria-label="Attorneys shaking hands with clients across a meeting table"></div>
<div class="abs hero-shade"></div>
<div class="abs rule dl dr" style="top:305px;left:437px;width:327px"></div>
<div class="abs hero-kicker">BRIGHTLINE LAW</div>
<div class="abs rule dl dr" style="top:351px;left:437px;width:327px"></div>
<h1 class="abs hero-title">HUSBAND, AND WIFE TEAM</h1>
<div class="abs hero-sub">IS HERE TO HELP YOU NAVIGATE THROUGH LIFE'S TOUGHER MOMENTS.</div>
<a class="abs btn hero-btn">CONTACT US</a>

<!-- about -->
<div class="abs about"></div>
<div class="abs about-tab"><div class="vertical up">ABOUT US</div></div>
<div class="abs about-photo photo" role="img" aria-label="Smiling couple looking at a tablet together"></div>
<div class="abs about-photo-small photo" role="img" aria-label="Judge's gavel and law books"></div>
<h2 class="abs about-title">BRIGHTLINE LAW</h2>
<div class="abs rule dr" style="top:860px;left:590px;width:424px"></div>
<div class="abs about-copy">
  <p>It is a long established fact that a reader will be distracted by the readable content of a page when looking at its layout. The point of using Lorem Ipsum is that it has a more-or-less normal distribution of letters, as opposed to using 'Content here, content here', making it look like readable English.</p>
  <p>Many desktop publishing packages and web page editors now use Lorem Ipsum as their default model text, and a search for 'lorem ipsum' will uncover many web sites still in their infancy. Various versions have evolved over the years, sometimes by accident, sometimes on purpose (injected humour and the like).</p>
</div>
<a class="abs btn about-btn">LEARN MORE ABOUT US</a>

<!-- since -->
<div class="abs rule dl" style="top:1375px;left:303px;width:165px"></div>
<h2 class="abs section-title" style="top:1352px">SINCE 2007</h2>
<div class="abs rule dr" style="top:1375px;left:728px;width:167px"></div>
<div class="abs stats">
  <div class="stat"><div class="num">200+</div><div class="label">Trust Administrations</div></div>
  <div class="stat"><div class="num">400+</div><div class="label">Estate Plans</div></div>
  <div class="stat featured"><div class="num">400+</div><div class="label">Litigation Clients</div></div>
  <div class="stat"><div class="num">100+</div><div class="label">Securities Cases</div></div>
</div>

<!-- practice -->
<div class="abs practice photo" role="img" aria-label="Dark blue courthouse columns background"></div>
<div class="abs vertical practice-vertical">PRACTICE AREAS</div>
<div class="abs rule dl" style="top:1745px;left:200px;width:180px"></div>
<h2 class="abs practice-title">AREAS OF PRACTICE</h2>
<div class="abs rule dr" style="top:1745px;left:826px;width:180px"></div>
<div class="abs cards" style="top:1804px">
  <div class="card"><div class="shot photo" role="img" aria-label="Derailed train" style="background:linear-gradient(160deg,#6d7d92,#c9a43a 55%,#3d4a5c)"></div><div class="label">TRAIN ACCIDENTS</div><div class="plus">+</div></div>
  <div class="card"><div class="shot photo" role="img" aria-label="Patient in a wheelchair in a hospital corridor" style="background:linear-gradient(160deg,#c7ccd3,#8fa6a6 55%,#54606c)"></div><div class="label">MEDICAL<br>MALPRACTICE</div><div class="plus">+</div></div>
  <div class="card"><div class="shot photo" role="img" aria-label="Man wearing a neck brace" style="background:linear-gradient(160deg,#e0e2e6,#7d6656 55%,#2e3c52)"></div><div class="label">PERSONAL<br>INJURY</div><div class="plus">+</div></div>
  <div class="card"><div class="shot photo" role="img" aria-label="Firefighters at a vehicle crash" style="background:linear-gradient(160deg,#2a2a2e,#a8352c 55%,#1e1e22)"></div><div class="label">CAR &amp; TRUCK<br>ACCIDENTS</div><div class="plus">+</div></div>
</div>
<div class="abs cards" style="top:2036px">
  <div class="card"><div class="shot photo" role="img" aria-label="Worker holding a faulty device" style="background:linear-gradient(160deg,#b7c1cc,#5b6f88 55%,#33404f)"></div><div class="label">DEFECTIVE DEVICES</div><div class="plus">+</div></div>
  <div class="card"><div class="shot photo" role="img" aria-label="Laboratory vials with pipette" style="background:linear-gradient(160deg,#e4eef6,#b8d4ea 55%,#e08a4a)"></div><div class="label">DANGEROUS DRUGS</div><div class="plus">+</div></div>
  <div class="card"><div class="shot photo" role="img" aria-label="Hands holding talcum powder" style="background:linear-gradient(160deg,#bfd9ee,#e6eef4 50%,#d9b79b)"></div><div class="label">TALCUM POWDER</div><div class="plus">+</div></div>
  <div class="card"><div class="shot photo" role="img" aria-label="Distressed person sitting alone in shadow" style="background:linear-gradient(160deg,#2e2a2a,#7a5a52 55%,#1e1a1a)"></div><div class="label">SEXUAL ABUSE</div><div class="plus">+</div></div>
</div>
<a class="abs btn practice-btn">VIEW ALL PRACTICE AREAS</a>

<!-- testimonials -->
<div class="abs testi-panel"></div>
<div class="abs badge-cell" style="top:2493px;left:0"><span class="badge-shape"></span></div>
<div class="abs badge-cell" style="top:2493px;left:209px"><span class="badge-shape square"></span></div>
<div class="abs badge-cell" style="top:2493px;left:418px"><span class="badge-shape"></span></div>
<div class="abs badge-cell" style="top:2647px;left:0"><span class="badge-shape square"></span></div>
<div class="abs badge-cell" style="top:2647px;left:209px"><span class="badge-shape square"></span></div>
<div class="abs badge-cell" style="top:2801px;left:0"><span class="badge-shape"></span></div>
<div class="abs vertical up testi-vertical">TESTIMONIALS</div>
<h2 class="abs testi-title">WHAT OUR<br>CLIENTS SAY</h2>
<div class="abs rule dl" style="top:2652px;left:744px;width:286px"></div>
<p class="abs testi-copy">There are many variations of passages of Lorem Ipsum available, but the majority have suffered alteration in some form, by injected humour, or randomised words which don't look even slightly believable. If you are going to use a passage of Lorem Ipsum, you need to be sure there isn't anything embarrassing hidden in the middle of text. All the Lorem Ipsum generators on the Internet tend to repeat predefined chunks as necessary, making this the first true generator on the Internet. It uses a dictionary of over 200 Latin words, combined with a handful of model sentence structures, to generate Lorem Ipsum which looks reasonable. The generated Lorem Ipsum is therefore always free from repetition, injected humour, or non-characteristic words etc.</p>
<div class="abs author"><span class="avatar" role="img" aria-label="Client portrait"></span>MARIAN K.</div>
<div class="abs stars">
  <svg width="17" height="16" viewBox="0 0 24 23"><polygon fill="#0677BA" points="12,0 15,8 24,8 17,14 20,23 12,17 4,23 7,14 0,8 9,8"/></svg>
  <svg width="17" height="16" viewBox="0 0 24 23"><polygon fill="#0677BA" points="12,0 15,8 24,8 17,14 20,23 12,17 4,23 7,14 0,8 9,8"/></svg>
  <svg width="17" height="16" viewBox="0 0 24 23"><polygon fill="#0677BA" points="12,0 15,8 24,8 17,14 20,23 12,17 4,23 7,14 0,8 9,8"/></svg>
  <svg width="17" height="16" viewBox="0 0 24 23"><polygon fill="#0677BA" points="12,0 15,8 24,8 17,14 20,23 12,17 4,23 7,14 0,8 9,8"/></svg>
  <svg width="17" height="16" viewBox="0 0 24 23"><polygon fill="#0677BA" points="12,0 15,8 24,8 17,14 20,23 12,17 4,23 7,14 0,8 9,8"/></svg>
</div>

<!-- blog -->
<div class="abs rule dl" style="top:3059px;left:276px;width:165px"></div>
<h2 class="abs section-title" style="top:3036px">LATEST BLOG</h2>
<div class="abs rule dr" style="top:3059px;left:760px;width:165px"></div>
<div class="abs blog">
  <article class="post"><div class="shot photo" role="img" aria-label="Scales of justice beside a lawyer signing papers" style="background:linear-gradient(160deg,#f1f1ef,#b9b2a4 55%,#4b4640)"></div>
    <div class="meta"><div class="meta-row"><span>&#9679; By : Admin</span><span>&#9638; Aug 25,2023</span></div>Lorem Ipsum is simply dummy text<br>of the printing and typesetting industry.</div></article>
  <article class="post"><div class="shot photo" role="img" aria-label="Two business people shaking hands" style="background:linear-gradient(160deg,#3a3a3c,#b8b4ae 50%,#2c2c2e)"></div>
    <div class="meta"><div class="meta-row"><span>&#9679; By : Admin</span><span>&#9638; Aug 25,2023</span></div>Lorem Ipsum is simply dummy text<br>of the printing and typesetting industry.</div></article>
  <article class="post"><div class="shot photo" role="img" aria-label="Lawyers talking in a bright office" style="background:linear-gradient(160deg,#dfe6ec,#6f7f90 55%,#27323f)"></div>
    <div class="meta"><div class="meta-row"><span>&#9679; By : Admin</span><span>&#9638; Aug 25,2023</span></div>Lorem Ipsum is simply dummy text<br>of the printing and typesetting industry.</div></article>
</div>

<!-- get started -->
<div class="abs start photo" role="img" aria-label="Dark blue courthouse columns background"></div>
<div class="abs start-panel"></div>
<div class="abs start-photo photo" role="img" aria-label="Confident attorney standing with arms crossed"></div>
<div class="abs start-call"></div>
<h2 class="abs start-title">LET'S GET STARTED.</h2>
<div class="abs rule dr" style="top:3666px;left:167px;width:340px"></div>
<p class="abs start-lead">"Lorem ipsum dolor sit amet, consectetur adipiscing elit, sed do eiusmod tempor incididunt ut labore et dolore magna aliqua.</p>
<div class="abs field" style="top:3746px;left:168px;width:193px">Full Name</div>
<div class="abs field" style="top:3746px;left:371px;width:194px">Your Email</div>
<div class="abs field" style="top:3785px;left:168px;width:193px">Your Phone</div>
<div class="abs field" style="top:3785px;left:371px;width:194px">Your Subject</div>
<div class="abs field big" style="top:3826px;left:168px;width:397px">Tell us about your case...</div>
<a class="abs btn submit">SUBMIT NOW</a>
<p class="abs call-copy">At vero eos et accusamus et iusto odio dignissimos ducimus qui blanditiis praesentium voluptatum deleniti atque.</p>
<div class="abs call-line">
  <svg width="16" height="16" viewBox="0 0 24 24" fill="none" stroke="#fff" stroke-width="1.8"><path d="M22 16.9v3a2 2 0 0 1-2.2 2 19.8 19.8 0 0 1-8.6-3.1 19.5 19.5 0 0 1-6-6A19.8 19.8 0 0 1 2.1 4.2 2 2 0 0 1 4.1 2h3a2 2 0 0 1 2 1.7c.1.9.4 1.8.7 2.7a2 2 0 0 1-.5 2.1L8 9.8a16 16 0 0 0 6 6l1.3-1.3a2 2 0 0 1 2.1-.4c.9.3 1.8.6 2.7.7a2 2 0 0 1 1.7 2z"/></svg>
  CALL NOW: <strong>555-014-2286</strong>
</div>

<!-- footer -->
<footer class="abs footer"></footer>
<div class="abs brand footer-brand">BRIGHTLINE<small>LAW</small></div>
<div class="abs footer-social"><span class="dot-icon"></span><span class="dot-icon"></span><span class="dot-icon"></span></div>
<div class="abs fcol" style="left:454px"><h4>Quick Links</h4><ul><li>Home</li><li>About</li><li>Areas of Practise</li><li>Media</li><li>Resources</li><li>Contact Us</li></ul></div>
<div class="abs fcol" style="left:662px"><h4>Practice Areas</h4><ul><li>Train Accidents</li><li>Medical Malpratice</li><li>Personal Injury</li><li>Defective Devices</li><li>Dangerous Drugs</li><li>Talcum Power</li></ul></div>
<div class="abs fcol" style="left:883px;width:160px"><h4>Contact Us</h4>
  <div class="contact-row"><svg width="9" height="12" viewBox="0 0 9 12" fill="none" stroke="#7BADD7"><path d="M4.5 11.5S.5 7 .5 4.5a4 4 0 0 1 8 0c0 2.5-4 7-4 7z"/></svg><span>Lorem Ipsum is simply dummy text of the printing and typesetting industry.</span></div>
  <div class="contact-row"><svg width="10" height="10" viewBox="0 0 24 24" fill="#7BADD7"><path d="M22 16.9v3a2 2 0 0 1-2.2 2A19.8 19.8 0 0 1 2.1 4.2 2 2 0 0 1 4.1 2h3a2 2 0 0 1 2 1.7l.7 2.7a2 2 0 0 1-.5 2.1L8 9.8a16 16 0 0 0 6 6l1.3-1.3a2 2 0 0 1 2.1-.4l2.7.7a2 2 0 0 1 1.9 2z"/></svg><span>555.014.2286</span></div>
  <div class="contact-row"><svg width="11" height="9" viewBox="0 0 12 9" fill="#7BADD7"><rect width="12" height="9"/></svg><span>info@brightlinelaw.com</span></div>
</div>
<div class="abs footer-line"></div>
<div class="abs copyright">Copyright 2023 <b>Brightline Law</b>. All rights Reserved.</div>
<div class="abs legal">Privacy Policy &nbsp;|&nbsp; Terms Of Conditions</div>
<p class="abs fineprint">Lorem Ipsum is simply dummy text of the printing and typesetting industry. Lorem Ipsum has been the industry's standard dummy text ever since the 1500s, when an unknown printer took a galley of type and scrambled it to make a type specimen book. It has survived not only five centuries, but also the leap into electronic typesetting, remaining essentially unchanged. It was popularised in the 1960s with the release of sheets containing Lorem Ipsum passages, and more recently with desktop publishing software.</p>

</body>
</html>
```